Locksmith, Safes, Security Systems, Camera Systems, Home Theater, Chip Keys & Remotes

Darnel Hoskins Owner
2871 Pemberly Vane Loop
Dothan, AL 36301
P 334-815-4092
F 334-527-3810
dhoskins@trevonmarts.com
www.trevonmarts.com
AL Lic #5827
*Maybe follow us on Facebook or Facebook symbol

```html
<!DOCTYPE html>
<html lang="en">
<head>
<meta charset="utf-8">
<title>Trevonmart's Lock &amp; Security – Business Card</title>
<link rel="stylesheet" href="https://fonts.googleapis.com/css2?family=Abel&family=Oswald:wght@500&family=Roboto+Condensed:wght@400;700&display=swap">
<style>
  :root {
    --brand-blue: #2e3a94;
    --ink: #2b2b2b;
    --card: #ffffff;
    --backdrop: #eceeed;
  }
  * { margin: 0; padding: 0; box-sizing: border-box; }
  html, body {
    width: 1200px; height: 839px; overflow: hidden;
    background: var(--backdrop);
  }
  .card {
    position: absolute; left: 136px; top: 132px;
    width: 912px; height: 565px;
    background: var(--card);
    border: 1px solid #e0e2e1;
    box-shadow: 0 2px 8px rgba(0,0,0,0.12);
  }
  .brand { position: absolute; left: 25px; top: 32px; display: flex; align-items: center; }
  .brand-mark { width: 98px; height: 140px; background: var(--brand-blue); border-radius: 4px; }
  .brand-name {
    margin-left: 30px; margin-top: 10px;
    font-family: "Roboto Condensed", sans-serif;
    color: var(--brand-blue); text-transform: uppercase; line-height: 1.15;
  }
  .brand-name .title { display: block; font-size: 36px; font-weight: 700; letter-spacing: 0.3px; }
  .brand-name .tagline { display: block; font-size: 18px; font-weight: 400; letter-spacing: 0.8px; padding-left: 28px; }

  .person {
    position: absolute; right: calc(912px - 313px); top: 226px;
    text-align: right;
  }
  .person-name {
    font-family: "Roboto Condensed", sans-serif; font-weight: 700;
    font-size: 27px; color: var(--brand-blue);
  }
  .person-role {
    font-family: "Abel", sans-serif; font-size: 27px; color: var(--ink); margin-top: 4px;
  }
  .license {
    font-family: "Abel", sans-serif; font-size: 23px; color: var(--brand-blue); margin-top: 30px;
  }
  .social-badge {
    display: inline-block; width: 34px; height: 34px; margin-top: 40px;
    border: 2px solid var(--brand-blue); border-radius: 3px;
  }

  .divider {
    position: absolute; left: 344px; top: 203px; width: 4px; height: 237px;
    background: var(--brand-blue);
  }

  .contact { position: absolute; left: 372px; top: 218px; list-style: none; }
  .contact li {
    display: flex; align-items: center; height: 43px; white-space: nowrap;
    font-family: "Abel", sans-serif; font-size: 26px; color: var(--ink);
  }
  .contact svg { width: 28px; height: 24px; margin-right: 14px; fill: var(--brand-blue); flex: none; }

  .services {
    position: absolute; left: 0; bottom: 0; width: 100%; height: 78px;
    background: var(--brand-blue);
    display: flex; align-items: center; justify-content: space-between;
    flex-wrap: nowrap; white-space: nowrap;
    padding: 0 18px;
    font-family: "Oswald", sans-serif; font-weight: 500; font-size: 24px;
    color: #ffffff; letter-spacing: -0.2px;
  }
  .services span { flex: none; }
  .services .sep { font-size: 18px; }
</style>
</head>
<body>
  <div class="card">
    <div class="brand">
      <div class="brand-mark"></div>
      <div class="brand-name">
        <span class="title">Trevonmart's</span>
        <span class="tagline">Lock &amp; Security</span>
      </div>
    </div>

    <div class="person">
      <div class="person-name">Darnel Hoskins</div>
      <div class="person-role">Owner</div>
      <div class="license">AL Lic #5827</div>
      <span class="social-badge" aria-label="Social page"></span>
    </div>

    <div class="divider"></div>

    <ul class="contact">
      <li>
        <svg viewBox="0 0 28 24" aria-hidden="true"><path d="M14 1 1 9h26z"/><rect x="3" y="10" width="22" height="3"/><rect x="5" y="13" width="4" height="8"/><rect x="12" y="13" width="4" height="8"/><rect x="19" y="13" width="4" height="8"/><rect x="2" y="21" width="24" height="2"/></svg>
        2871 Pemberly Vane Loop Dothan, AL 36301
      </li>
      <li>
        <svg viewBox="0 0 28 24" aria-hidden="true"><path d="M8 2c1-1 2-1 3 0l2 3c.6 1 .3 2-.5 2.6L11 9c1 2.5 3 4.8 5.5 6l1.4-1.5c.7-.8 1.8-1 2.6-.4l3 2c1 .7 1 1.8.2 2.7l-2 2c-1.5 1.5-4 1.5-7-.5C10 16.5 7 13 5.8 9.5 4.8 6.5 5 4.5 6.5 3.2z"/></svg>
        334-815-4092
      </li>
      <li>
        <svg viewBox="0 0 28 24" aria-hidden="true"><rect x="8" y="1" width="12" height="7" fill="none" stroke="#2e3a94" stroke-width="2"/><rect x="3" y="9" width="22" height="8" rx="2"/><rect x="6" y="18" width="16" height="5" fill="none" stroke="#2e3a94" stroke-width="2"/></svg>
        334-527-3810
      </li>
      <li>
        <svg viewBox="0 0 28 24" aria-hidden="true"><path d="M3 4h22v16H3z M5 6v1l9 6 9-6V6z M5 9.5V18h18V9.5l-9 6z" fill-rule="evenodd"/></svg>
        dhoskins@trevonmarts.com
      </li>
      <li>
        <svg viewBox="0 0 28 24" aria-hidden="true"><g fill="none" stroke="#2e3a94" stroke-width="2"><circle cx="14" cy="12" r="10"/><ellipse cx="14" cy="12" rx="4.5" ry="10"/><path d="M4 12h20M6 6h16M6 18h16"/></g></svg>
        www.trevonmarts.com
      </li>
    </ul>

    <div class="services">
      <span>Locksmith</span><span class="sep">•</span>
      <span>Safes</span><span class="sep">•</span>
      <span>Security Systems</span><span class="sep">•</span>
      <span>Camera Systems</span><span class="sep">•</span>
      <span>Home Theater</span><span class="sep">•</span>
      <span>Chip Keys &amp; Remotes</span>
    </div>
  </div>
</body>
</html>
```